WooCommerce Web Design for SEO Agency

Looking for a clean and fast WooCommerce design

Selling 5 different products each with maybe 3-4 variants

Need imagery - featured images, basic logo etc

I will supply all content and most is ready to go (or can be in a few days)

You will need to design and build the site including some basic WooCommerce configuration - PayPal, checkout forms etc

Target Market(s)

SEO, Internet marketers

Coding

Coded - Design and coding required

Number of Pages Required

3 page

Font styles to use
Sans Serif

Requirements
Must have
• WooCommerce and WP integration

```html
<!DOCTYPE html>
<html lang="en">
<head>
<meta charset="utf-8">
<title>Linkwise – Home page variations</title>
<link href="https://fonts.googleapis.com/css2?family=Roboto:wght@300;400;500;700&family=Rubik:wght@500;700&family=Poppins:wght@400;500&display=swap" rel="stylesheet">
<style>
:root{
  --blue:#3b74d8;
  --teal:#12cdb5;
  --ink:#222633;
  --nav:#2b2f3e;
  --foot:#0e1320;
  --muted:#8a8f9c;
  --soft:#f2f5fa;
  --line:#e6e9f0;
  --white:#ffffff;
}
*{box-sizing:border-box;margin:0;padding:0}
html,body{width:1077px;height:1200px;overflow:hidden;background:#fff}
body{position:relative;font-family:"Poppins",sans-serif;color:var(--ink)}
.page{position:absolute;top:39px;width:530px;height:1894px;transform:scale(.5943);transform-origin:0 0;background:#fff;box-shadow:0 6px 30px rgba(20,30,60,.25);overflow:hidden}
.page--a{left:41px}.page--b{left:383px}.page--c{left:725px}
section,header,nav,footer{position:relative;width:530px}
.abs{position:absolute}
/* header */
.site-header{height:46px;background:#fff}
.brand{position:absolute;left:50px;top:14px;font:500 11px "Roboto",sans-serif;color:var(--ink);display:flex;align-items:center;gap:4px}
.brand i{width:7px;height:7px;background:var(--blue);display:block}
.contact{position:absolute;top:15px;display:flex;align-items:center;gap:5px;font-size:4.5px;color:var(--ink)}
.contact b{display:block;font-weight:400;color:var(--muted)}
.contact .ic{width:16px;height:16px;border:1px solid var(--blue);border-radius:50%;display:flex;align-items:center;justify-content:center}
.btn{display:inline-flex;align-items:center;justify-content:center;font:500 5px "Poppins",sans-serif;letter-spacing:.3px;border-radius:2px;text-transform:uppercase}
.btn--solid{background:var(--blue);color:#fff}
.btn--ghost{border:1px solid #fff;color:#fff}
.login{position:absolute;left:422px;top:16px;width:54px;height:16px}
.site-nav{height:27px;background:var(--nav);display:flex;align-items:center;justify-content:flex-end;padding-right:52px;gap:12px;font:500 4.6px "Poppins",sans-serif;color:#fff}
.site-nav .tool{width:14px;height:27px;display:flex;align-items:center;justify-content:center;border-left:1px solid #454a5b}
/* hero */
.hero{height:257px;overflow:hidden}
.hero--grad{background:linear-gradient(110deg,#3a73dc 0%,#2b9ad8 45%,#0fd0b2 100%)}
.hero--photo{background:linear-gradient(120deg,#2f4f8f 0%,#3d7fb0 50%,#4fb7a8 100%)}
.hero--blob{background:#fff}
.hero h1{position:absolute;font:700 18px "Rubik",sans-serif;letter-spacing:.3px;color:#fff}
.hero p{position:absolute;font-size:6.3px;line-height:9px;color:#fff}
.hero .cta{position:absolute;width:72px;height:16px}
.dots{position:absolute;display:flex;gap:4px}
.dots span{width:4px;height:4px;border-radius:50%;border:1px solid #fff}
.dots span:first-child{background:#fff}
.art{position:absolute}
/* section heads */
.sec-title{position:absolute;left:0;width:530px;text-align:center;font:400 14px "Roboto",sans-serif;letter-spacing:.2px;text-transform:uppercase}
.rule{position:absolute;height:1px;width:28px;background:var(--blue)}
.rule::after{content:"";position:absolute;left:11px;top:-2px;width:5px;height:5px;border-radius:50%;background:var(--blue)}
.sec-sub{position:absolute;left:165px;width:200px;text-align:center;font-size:5.5px;line-height:8.5px;color:var(--muted)}
/* about */
.about{height:249px}
.about h2{position:absolute;font:400 14px "Roboto",sans-serif}
.about h3{position:absolute;font:400 8.5px "Roboto",sans-serif}
.about p{position:absolute;width:198px;font-size:5.2px;line-height:8px;color:var(--muted);text-align:justify}
.about .more{position:absolute;width:61px;height:16px}
/* services */
.services{height:297px;background:var(--soft)}
.card{position:absolute;top:103px;width:137px;height:142px;background:#fff;box-shadow:0 2px 8px rgba(30,50,90,.08);text-align:center}
.card--on{background:linear-gradient(135deg,#3a73dc,#10d0b3);color:#fff}
.card .icon{width:28px;height:28px;border-radius:50%;margin:16px auto 0;display:flex;align-items:center;justify-content:center}
.card h4{font:400 9.5px "Roboto",sans-serif;margin-top:11px}
.card p{font-size:4.4px;line-height:8px;color:var(--muted);padding:0 7px;margin-top:7px}
.card--on p{color:#eaf6ff}
.card .btn{width:61px;height:16px;margin-top:8px}
.bar-dots{position:absolute;left:257px;display:flex;gap:3px}
.bar-dots span{width:3px;height:3px;border-radius:50%;background:#a8c0ec}
.bar-dots span:first-child{width:10px;border-radius:2px;background:var(--blue)}
/* testimonials */
.testimonials{height:253px}
.quote-card{position:absolute;left:134px;top:95px;width:262px;height:120px;background:#fff;box-shadow:0 2px 10px rgba(30,50,90,.09);text-align:center}
.quote-card .mark{font:700 22px "Rubik",sans-serif;color:var(--blue);margin-top:4px;height:20px}
.quote-card p{font-size:4.6px;line-height:8.3px;color:var(--muted);padding:0 12px;margin-top:6px}
.person{display:flex;align-items:center;justify-content:center;gap:5px;margin-top:8px;text-align:left}
.person .av{width:20px;height:20px;border-radius:50%;background:#d9cbb8}
.person b{display:block;font:500 6px "Poppins",sans-serif}
.person span{font-size:4.5px;color:var(--muted)}
.arrow{position:absolute;top:143px;width:17px;height:17px;border:1px solid var(--blue);border-radius:50%;display:flex;align-items:center;justify-content:center}
/* stats */
.stats{height:252px;background:var(--soft)}
.stat{position:absolute;top:108px;width:80px;text-align:center}
.stat b{display:block;font:700 18px "Rubik",sans-serif;color:var(--blue);line-height:20px}
.stat span{font-size:5.5px}
.ask{position:absolute;left:108px;top:170px;width:272px;height:45px;background:#fff;box-shadow:0 2px 8px rgba(30,50,90,.06)}
.ask h5{position:absolute;left:16px;top:11px;font:400 8.5px "Roboto",sans-serif}
.ask p{position:absolute;left:16px;top:27px;font-size:6px;color:var(--muted)}
.ask .btn{position:absolute;left:196px;top:14px;width:61px;height:16px}
/* blog */
.blog{height:321px}
.post{position:absolute;top:99px;width:137px;height:184px;background:#fff;box-shadow:0 2px 8px rgba(30,50,90,.08)}
.post .thumb{height:92px}
.post .meta{font-size:4.2px;color:var(--muted);padding:6px 6px 0}
.post h6{font:400 8px "Roboto",sans-serif;padding:6px 6px 0}
.post p{font-size:4.2px;line-height:7.5px;color:var(--muted);padding:5px 6px 0}
.post a{display:block;font-size:5px;color:var(--blue);padding:7px 6px 0;text-decoration:none}
/* footer */
.site-footer{height:192px;background:var(--foot);color:#fff}
.site-footer .brand{color:#fff;top:22px}
.f-about{position:absolute;left:50px;top:68px;width:120px;font-size:4.7px;line-height:7.5px;color:#c9cdd8}
.socials{position:absolute;left:50px;top:122px;display:flex;gap:8px}
.socials span{width:12px;height:12px;border-radius:50%;background:#fff}
.f-col{position:absolute;top:38px}
.f-col h6{font:500 9px "Roboto",sans-serif;margin-bottom:8px}
.f-col li{list-style:none;font-size:4.8px;line-height:10.5px;color:#c9cdd8}
.f-col .addr{font-size:4.8px;line-height:7.5px;color:#c9cdd8;width:125px;margin-bottom:12px}
.f-col .addr b{color:#fff;font-weight:500}
.copy{position:absolute;left:0;width:530px;top:172px;text-align:center;font-size:4.5px;color:#c9cdd8}
</style>
</head>
<body>

<!-- ============ VARIATION A ============ -->
<div class="page page--a">
  <header class="site-header">
    <div class="brand"><i></i>Linkwise</div>
    <div class="contact" style="left:245px"><span class="ic"><svg width="8" height="8" viewBox="0 0 24 24"><path d="M6 2l4 4-2 3a12 12 0 007 7l3-2 4 4-3 4C10 21 3 14 2 5z" fill="none" stroke="#3b74d8" stroke-width="2"/></svg></span><div><b>Call Us:</b>+1 555 010 0142</div></div>
    <div class="contact" style="left:325px"><span class="ic"><svg width="8" height="8" viewBox="0 0 24 24"><rect x="2" y="5" width="20" height="14" fill="none" stroke="#3b74d8" stroke-width="2"/><path d="M2 5l10 8 10-8" fill="none" stroke="#3b74d8" stroke-width="2"/></svg></span><div><b>Email Us:</b>hello@linkwise.example</div></div>
    <span class="btn btn--solid login">Login</span>
  </header>
  <nav class="site-nav"><span>HOME</span><span>ABOUT US ▾</span><span>SERVICES ▾</span><span>TESTIMONIALS</span><span>BLOG</span><span>CONTACT US</span><span class="tool"><svg width="9" height="8" viewBox="0 0 24 22"><path d="M1 2h4l3 12h12l3-9H7" fill="none" stroke="#fff" stroke-width="2"/><circle cx="10" cy="19" r="2" fill="#fff"/><circle cx="18" cy="19" r="2" fill="#fff"/></svg></span><span class="tool"><svg width="7" height="7" viewBox="0 0 24 24"><circle cx="10" cy="10" r="7" fill="none" stroke="#fff" stroke-width="3"/><path d="M15 15l7 7" stroke="#fff" stroke-width="3"/></svg></span></nav>
  <section class="hero hero--grad">
    <h1 style="left:56px;top:80px">SEO LINK BUILDING</h1>
    <p style="left:56px;top:108px;width:240px">Lorem ipsum dolor sit amet, consectetur adipiscing elit, sed do eiusmod tempor incididunt.</p>
    <span class="btn btn--ghost cta" style="left:56px;top:140px">Get Started</span>
    <div class="art" role="img" aria-label="Isometric illustration of a monitor with linked web pages and gears" style="left:305px;top:62px;width:200px;height:145px;background:linear-gradient(135deg,rgba(255,255,255,.35),rgba(232,73,150,.45));border-radius:10px"></div>
    <div class="dots" style="left:255px;top:224px"><span></span><span></span><span></span></div>
  </section>
  <section class="about">
    <div class="art" role="img" aria-label="Illustration of browser windows joined by a chain link on a blue-teal blob" style="left:35px;top:20px;width:215px;height:215px;background:linear-gradient(135deg,#3a73dc,#10d0b3);border-radius:48% 52% 40% 60% / 55% 45% 55% 45%"></div>
    <h2 style="left:281px;top:36px">ABOUT US</h2><span class="rule" style="left:281px;top:56px"></span>
    <h3 style="left:281px;top:68px">Lorem ipsum dolor sit amet, consectetur</h3>
    <p style="left:281px;top:90px">Molestias excepturi sint occaecati cupiditate nonkuseopi iousesios provident, similique sunt in culpa qui officia deserunt mollitiaseiu animi, id est laborum et dolorum fuga.</p>
    <p style="left:281px;top:130px">Et harum quidem rerum facilis est et expedita distinctio. Nam libero tempore, cum soluta nobis est eligendi optio cumque nihil impedit quo minus id quod maxime placeat facere possimus, omnis voluptas.</p>
    <span class="btn btn--solid more" style="left:281px;top:183px">Read More</span>
  </section>
  <section class="services">
    <div class="sec-title" style="top:35px">Our Services</div><span class="rule" style="left:251px;top:55px"></span>
    <div class="sec-sub" style="top:61px">Lorem ipsum dolor sit amet, consectetur adipiscing elit, sed do eiusmod tempor incididunt</div>
    <div class="card" style="left:48px"><div class="icon" style="background:#fde3ea"><svg width="10" height="10" viewBox="0 0 24 24"><rect x="3" y="5" width="18" height="14" rx="2" fill="none" stroke="#e6497e" stroke-width="2"/></svg></div><h4>Backlinks</h4><p>Lorem ipsum dolor sit amet, consectetur adipiscing elit, sed do eiusmod tempor incididunt ut labore et dolore magna aliqua.</p><span class="btn btn--solid">Read More</span></div>
    <div class="card card--on" style="left:196px"><div class="icon" style="background:#fff"><svg width="10" height="10" viewBox="0 0 24 24"><rect x="3" y="4" width="18" height="16" rx="2" fill="none" stroke="#3b74d8" stroke-width="2"/><path d="M3 9h18" stroke="#3b74d8" stroke-width="2"/></svg></div><h4>Content writing</h4><p>Lorem ipsum dolor sit amet, consectetur adipiscing elit, sed do eiusmod tempor incididunt ut labore et dolore magna aliqua.</p><span class="btn btn--ghost">Read More</span></div>
    <div class="card" style="left:344px"><div class="icon" style="background:#dff5e6"><svg width="10" height="10" viewBox="0 0 24 24"><rect x="3" y="4" width="18" height="13" rx="2" fill="none" stroke="#3cb46e" stroke-width="2"/><path d="M8 21h8" stroke="#3cb46e" stroke-width="2"/></svg></div><h4>Digital PR for Links</h4><p>Lorem ipsum dolor sit amet, consectetur adipiscing elit, sed do eiusmod tempor incididunt ut labore et dolore magna aliqua.</p><span class="btn btn--solid">Read More</span></div>
    <div class="bar-dots" style="top:257px"><span></span><span></span></div>
  </section>
  <section class="testimonials">
    <div class="sec-title" style="top:37px">Testimonials</div><span class="rule" style="left:251px;top:57px"></span>
    <div class="sec-sub" style="top:63px">Lorem ipsum dolor sit amet, consectetur adipiscing elit, sed do eiusmod tempor incididunt</div>
    <span class="arrow" style="left:92px"><svg width="5" height="5" viewBox="0 0 10 10"><path d="M7 1L3 5l4 4" fill="none" stroke="#3b74d8" stroke-width="1.5"/></svg></span>
    <div class="quote-card"><div class="mark">“</div><p>Similique sunt in culpa qui officia deserunt mollitia animi, id est laborum et dolorum fuga. Et harum quidem rerum facilis est et expedita distinctio. Nam libero tempore, cum soluta nobis est eligendi optio cumque nihil impedit quo.</p><div class="person"><span class="av"></span><div><b>Dana Reyes</b><span>CEO, Northfield</span></div></div></div>
    <span class="arrow" style="left:421px"><svg width="5" height="5" viewBox="0 0 10 10"><path d="M3 1l4 4-4 4" fill="none" stroke="#3b74d8" stroke-width="1.5"/></svg></span>
  </section>
  <section class="stats">
    <div class="sec-title" style="top:36px">Customers Expectation</div><span class="rule" style="left:251px;top:56px"></span>
    <div class="sec-sub" style="top:62px">Lorem ipsum dolor sit amet, consectetur adipiscing elit, sed do eiusmod tempor incididunt</div>
    <div class="stat" style="left:68px"><b>120k</b><span>Downloaded</span></div>
    <div class="stat" style="left:162px"><b>7k</b><span>Feedback</span></div>
    <div class="stat" style="left:258px"><b>150+</b><span>Workers</span></div>
    <div class="stat" style="left:359px"><b>35+</b><span>Contributors</span></div>
    <div class="ask"><h5>HAVE ANY QUESTIONS ABOUT US?</h5><p>Don't hesitate to contact us</p><span class="btn btn--solid">Read More</span></div>
  </section>
  <section class="blog">
    <div class="sec-title" style="top:37px">Our Blog</div><span class="rule" style="left:251px;top:57px"></span>
    <div class="sec-sub" style="top:63px">Lorem ipsum dolor sit amet, consectetur adipiscing elit, sed do eiusmod tempor incididunt</div>
    <article class="post" style="left:48px"><div class="thumb" role="img" aria-label="Photo of wooden blocks with marketing icons on a desk" style="background:linear-gradient(135deg,#8a5a34,#c99b6c)"></div><div class="meta">Admin &nbsp; May 18, 2020</div><h6>Dignissimos Ucimus</h6><p>Lorem ipsum dolor sit amet, aseiu consectetur adipiscing elit, sed dsaeujo sei eiusmod tempor incididunt ut labore</p><a>Read More ›</a></article>
    <article class="post" style="left:196px"><div class="thumb" role="img" aria-label="Photo of a desk with a sketched link building note" style="background:linear-gradient(135deg,#d8d4cc,#f4f1ea)"></div><div class="meta">Admin &nbsp; May 18, 2020</div><h6>Dignissimos Ucimus</h6><p>Lorem ipsum dolor sit amet, aseiu consectetur adipiscing elit, sed dsaeujo sei eiusmod tempor incididunt ut labore</p><a>Read More ›</a></article>
    <article class="post" style="left:344px"><div class="thumb" role="img" aria-label="Photo of a keyboard with an orange web traffic key" style="background:linear-gradient(135deg,#3a3d44,#e9a23b)"></div><div class="meta">Admin &nbsp; May 18, 2020</div><h6>Dignissimos Ucimus</h6><p>Lorem ipsum dolor sit amet, aseiu consectetur adipiscing elit, sed dsaeujo sei eiusmod tempor incididunt ut labore</p><a>Read More ›</a></article>
  </section>
  <footer class="site-footer">
    <div class="brand"><i></i>Linkwise</div>
    <p class="f-about">architecto beatae vitae dicta sunt oisauerk explicabo. Nemo enim ipsam voluptatem quia voluptas sit aspernatur aut odit aut fugitsaeiu klasdmoix.</p>
    <div class="socials"><span></span><span></span><span></span></div>
    <div class="f-col" style="left:178px"><h6>Quick Links</h6><ul><li>Home</li><li>About Us</li><li>Services</li><li>Testimonials</li><li>Blog</li><li>Contact Us</li></ul></div>
    <div class="f-col" style="left:278px"><h6>Support</h6><ul><li>FAQ's</li><li>Privacy Policy</li><li>Terms &amp; Condition</li><li>Community</li><li>Contact Us</li></ul></div>
    <div class="f-col" style="left:380px"><h6>Address</h6><p class="addr"><b>Location:</b> 120 Harbor Lane, San Diego, CA 92101, USA</p><p class="addr"><b>Email:</b> hello@linkwise.example</p><p class="addr"><b>Phone:</b> +1 555 010 0142</p></div>
    <div class="copy">Copyright ©2020 All rights reserved</div>
  </footer>
</div>

<!-- ============ VARIATION B ============ -->
<div class="page page--b">
  <header class="site-header">
    <div class="brand"><i></i>Linkwise</div>
    <div class="contact" style="left:245px"><span class="ic"><svg width="8" height="8" viewBox="0 0 24 24"><path d="M6 2l4 4-2 3a12 12 0 007 7l3-2 4 4-3 4C10 21 3 14 2 5z" fill="none" stroke="#3b74d8" stroke-width="2"/></svg></span><div><b>Call Us:</b>+1 555 010 0142</div></div>
    <div class="contact" style="left:325px"><span class="ic"><svg width="8" height="8" viewBox="0 0 24 24"><rect x="2" y="5" width="20" height="14" fill="none" stroke="#3b74d8" stroke-width="2"/><path d="M2 5l10 8 10-8" fill="none" stroke="#3b74d8" stroke-width="2"/></svg></span><div><b>Email Us:</b>hello@linkwise.example</div></div>
    <span class="btn btn--solid login">Login</span>
  </header>
  <nav class="site-nav"><span>HOME</span><span>ABOUT US ▾</span><span>SERVICES ▾</span><span>TESTIMONIALS</span><span>BLOG</span><span>CONTACT US</span><span class="tool"><svg width="9" height="8" viewBox="0 0 24 22"><path d="M1 2h4l3 12h12l3-9H7" fill="none" stroke="#fff" stroke-width="2"/><circle cx="10" cy="19" r="2" fill="#fff"/><circle cx="18" cy="19" r="2" fill="#fff"/></svg></span><span class="tool"><svg width="7" height="7" viewBox="0 0 24 24"><circle cx="10" cy="10" r="7" fill="none" stroke="#fff" stroke-width="3"/><path d="M15 15l7 7" stroke="#fff" stroke-width="3"/></svg></span></nav>
  <section class="hero hero--photo" role="img" aria-label="Photo of a businessman touching a digital screen of client icons, tinted blue-teal">
    <h1 style="left:0;width:530px;text-align:center;top:80px">SEO LINK BUILDING</h1>
    <p style="left:115px;top:108px;width:300px;text-align:center">Lorem ipsum dolor sit amet, consectetur adipiscing elit, sed do eiusmod tempor incididunt ut labore et dolore magna aliqua.</p>
    <span class="btn btn--ghost cta" style="left:229px;top:140px">Get Started</span>
    <div class="dots" style="left:255px;top:224px"><span></span><span></span><span></span></div>
  </section>
  <section class="about">
    <h2 style="left:49px;top:36px">ABOUT US</h2><span class="rule" style="left:49px;top:56px"></span>
    <h3 style="left:49px;top:68px">Lorem ipsum dolor sit amet, consectetur</h3>
    <p style="left:49px;top:90px">Molestias excepturi sint occaecati cupiditate nonkuseopi iousesios provident, similique sunt in culpa qui officia deserunt mollitiaseiu animi, id est laborum et dolorum fuga.</p>
    <p style="left:49px;top:130px">Et harum quidem rerum facilis est et expedita distinctio. Nam libero tempore, cum soluta nobis est eligendi optio cumque nihil impedit quo minus id quod maxime placeat facere possimus, omnis voluptas.</p>
    <span class="btn btn--solid more" style="left:49px;top:183px">Read More</span>
    <div class="abs" style="left:273px;top:33px;width:212px;height:186px;background:#fff;box-shadow:0 2px 8px rgba(30,50,90,.1)"></div>
    <div class="art" role="img" aria-label="Photo of a glowing chain link over dark binary code" style="left:281px;top:38px;width:200px;height:174px;background:linear-gradient(135deg,#0d1a2e,#1f5a78 60%,#0d1a2e)"></div>
  </section>
  <section class="services">
    <div class="sec-title" style="top:35px">Our Services</div><span class="rule" style="left:251px;top:55px"></span>
    <div class="sec-sub" style="top:61px">Lorem ipsum dolor sit amet, consectetur adipiscing elit, sed do eiusmod tempor incididunt</div>
    <div class="card" style="left:48px"><div class="icon" style="background:#fde3ea"><svg width="10" height="10" viewBox="0 0 24 24"><rect x="3" y="5" width="18" height="14" rx="2" fill="none" stroke="#e6497e" stroke-width="2"/></svg></div><h4>Backlinks</h4><p>Lorem ipsum dolor sit amet, consectetur adipiscing elit, sed do eiusmod tempor incididunt ut labore et dolore magna aliqua.</p><span class="btn btn--solid">Read More</span></div>
    <div class="card card--on" style="left:196px"><div class="icon" style="background:#fff"><svg width="10" height="10" viewBox="0 0 24 24"><rect x="3" y="4" width="18" height="16" rx="2" fill="none" stroke="#3b74d8" stroke-width="2"/><path d="M3 9h18" stroke="#3b74d8" stroke-width="2"/></svg></div><h4>Content writing</h4><p>Lorem ipsum dolor sit amet, consectetur adipiscing elit, sed do eiusmod tempor incididunt ut labore et dolore magna aliqua.</p><span class="btn btn--ghost">Read More</span></div>
    <div class="card" style="left:344px"><div class="icon" style="background:#dff5e6"><svg width="10" height="10" viewBox="0 0 24 24"><rect x="3" y="4" width="18" height="13" rx="2" fill="none" stroke="#3cb46e" stroke-width="2"/><path d="M8 21h8" stroke="#3cb46e" stroke-width="2"/></svg></div><h4>Digital PR for Links</h4><p>Lorem ipsum dolor sit amet, consectetur adipiscing elit, sed do eiusmod tempor incididunt ut labore et dolore magna aliqua.</p><span class="btn btn--solid">Read More</span></div>
    <div class="bar-dots" style="top:257px"><span></span><span></span></div>
  </section>
  <section class="testimonials">
    <div class="sec-title" style="top:37px">Testimonials</div><span class="rule" style="left:251px;top:57px"></span>
    <div class="sec-sub" style="top:63px">Lorem ipsum dolor sit amet, consectetur adipiscing elit, sed do eiusmod tempor incididunt</div>
    <span class="arrow" style="left:92px"><svg width="5" height="5" viewBox="0 0 10 10"><path d="M7 1L3 5l4 4" fill="none" stroke="#3b74d8" stroke-width="1.5"/></svg></span>
    <div class="quote-card"><div class="mark">“</div><p>Similique sunt in culpa qui officia deserunt mollitia animi, id est laborum et dolorum fuga. Et harum quidem rerum facilis est et expedita distinctio. Nam libero tempore, cum soluta nobis est eligendi optio cumque nihil impedit quo.</p><div class="person"><span class="av"></span><div><b>Dana Reyes</b><span>CEO, Northfield</span></div></div></div>
    <span class="arrow" style="left:421px"><svg width="5" height="5" viewBox="0 0 10 10"><path d="M3 1l4 4-4 4" fill="none" stroke="#3b74d8" stroke-width="1.5"/></svg></span>
  </section>
  <section class="stats">
    <div class="sec-title" style="top:36px">Customers Expectation</div><span class="rule" style="left:251px;top:56px"></span>
    <div class="sec-sub" style="top:62px">Lorem ipsum dolor sit amet, consectetur adipiscing elit, sed do eiusmod tempor incididunt</div>
    <div class="stat" style="left:68px"><b>120k</b><span>Downloaded</span></div>
    <div class="stat" style="left:162px"><b>7k</b><span>Feedback</span></div>
    <div class="stat" style="left:258px"><b>150+</b><span>Workers</span></div>
    <div class="stat" style="left:359px"><b>35+</b><span>Contributors</span></div>
    <div class="ask"><h5>HAVE ANY QUESTIONS ABOUT US?</h5><p>Don't hesitate to contact us</p><span class="btn btn--solid">Read More</span></div>
  </section>
  <section class="blog">
    <div class="sec-title" style="top:37px">Our Blog</div><span class="rule" style="left:251px;top:57px"></span>
    <div class="sec-sub" style="top:63px">Lorem ipsum dolor sit amet, consectetur adipiscing elit, sed do eiusmod tempor incididunt</div>
    <article class="post" style="left:48px"><div class="thumb" role="img" aria-label="Photo of wooden blocks with marketing icons on a desk" style="background:linear-gradient(135deg,#8a5a34,#c99b6c)"></div><div class="meta">Admin &nbsp; May 18, 2020</div><h6>Dignissimos Ucimus</h6><p>Lorem ipsum dolor sit amet, aseiu consectetur adipiscing elit, sed dsaeujo sei eiusmod tempor incididunt ut labore</p><a>Read More ›</a></article>
    <article class="post" style="left:196px"><div class="thumb" role="img" aria-label="Photo of a desk with a sketched link building note" style="background:linear-gradient(135deg,#d8d4cc,#f4f1ea)"></div><div class="meta">Admin &nbsp; May 18, 2020</div><h6>Dignissimos Ucimus</h6><p>Lorem ipsum dolor sit amet, aseiu consectetur adipiscing elit, sed dsaeujo sei eiusmod tempor incididunt ut labore</p><a>Read More ›</a></article>
    <article class="post" style="left:344px"><div class="thumb" role="img" aria-label="Photo of a keyboard with an orange web traffic key" style="background:linear-gradient(135deg,#3a3d44,#e9a23b)"></div><div class="meta">Admin &nbsp; May 18, 2020</div><h6>Dignissimos Ucimus</h6><p>Lorem ipsum dolor sit amet, aseiu consectetur adipiscing elit, sed dsaeujo sei eiusmod tempor incididunt ut labore</p><a>Read More ›</a></article>
  </section>
  <footer class="site-footer">
    <div class="brand"><i></i>Linkwise</div>
    <p class="f-about">architecto beatae vitae dicta sunt oisauerk explicabo. Nemo enim ipsam voluptatem quia voluptas sit aspernatur aut odit aut fugitsaeiu klasdmoix.</p>
    <div class="socials"><span></span><span></span><span></span></div>
    <div class="f-col" style="left:178px"><h6>Quick Links</h6><ul><li>Home</li><li>About Us</li><li>Services</li><li>Testimonials</li><li>Blog</li><li>Contact Us</li></ul></div>
    <div class="f-col" style="left:278px"><h6>Support</h6><ul><li>FAQ's</li><li>Privacy Policy</li><li>Terms &amp; Condition</li><li>Community</li><li>Contact Us</li></ul></div>
    <div class="f-col" style="left:380px"><h6>Address</h6><p class="addr"><b>Location:</b> 120 Harbor Lane, San Diego, CA 92101, USA</p><p class="addr"><b>Email:</b> hello@linkwise.example</p><p class="addr"><b>Phone:</b> +1 555 010 0142</p></div>
    <div class="copy">Copyright ©2020 All rights reserved</div>
  </footer>
</div>

<!-- ============ VARIATION C ============ -->
<div class="page page--c">
  <header class="site-header">
    <div class="brand"><i></i>Linkwise</div>
    <div class="contact" style="left:245px"><span class="ic"><svg width="8" height="8" viewBox="0 0 24 24"><path d="M6 2l4 4-2 3a12 12 0 007 7l3-2 4 4-3 4C10 21 3 14 2 5z" fill="none" stroke="#3b74d8" stroke-width="2"/></svg></span><div><b>Call Us:</b>+1 555 010 0142</div></div>
    <div class="contact" style="left:325px"><span class="ic"><svg width="8" height="8" viewBox="0 0 24 24"><rect x="2" y="5" width="20" height="14" fill="none" stroke="#3b74d8" stroke-width="2"/><path d="M2 5l10 8 10-8" fill="none" stroke="#3b74d8" stroke-width="2"/></svg></span><div><b>Email Us:</b>hello@linkwise.example</div></div>
    <span class="btn btn--solid login">Login</span>
  </header>
  <nav class="site-nav"><span>HOME</span><span>ABOUT US ▾</span><span>SERVICES ▾</span><span>TESTIMONIALS</span><span>BLOG</span><span>CONTACT US</span><span class="tool"><svg width="9" height="8" viewBox="0 0 24 22"><path d="M1 2h4l3 12h12l3-9H7" fill="none" stroke="#fff" stroke-width="2"/><circle cx="10" cy="19" r="2" fill="#fff"/><circle cx="18" cy="19" r="2" fill="#fff"/></svg></span><span class="tool"><svg width="7" height="7" viewBox="0 0 24 24"><circle cx="10" cy="10" r="7" fill="none" stroke="#fff" stroke-width="3"/><path d="M15 15l7 7" stroke="#fff" stroke-width="3"/></svg></span></nav>
  <section class="hero hero--blob">
    <svg class="abs" style="left:205px;top:0" width="325" height="257" viewBox="0 0 325 257"><defs><linearGradient id="blobC" x1="0" y1="1" x2="1" y2="0"><stop offset="0" stop-color="#3a73dc"/><stop offset="1" stop-color="#10d0b3"/></linearGradient></defs><path d="M325 0H160C120 40 90 90 50 150C10 210 0 255 60 254C140 252 250 250 325 257Z" fill="url(#blobC)"/></svg>
    <h1 style="left:56px;top:80px;color:var(--blue)">SEO LINK BUILDING</h1>
    <p style="left:56px;top:108px;width:240px;color:var(--ink)">Lorem ipsum dolor sit amet, consectetur adipiscing elit, sed do eiusmod tempor incididunt.</p>
    <span class="btn cta" style="left:56px;top:140px;border:1px solid var(--blue);color:var(--blue)">Get Started</span>
    <div class="art" role="img" aria-label="Isometric illustration of a monitor with linked web pages and gears" style="left:305px;top:50px;width:200px;height:150px;background:linear-gradient(135deg,rgba(255,255,255,.35),rgba(232,73,150,.45));border-radius:10px"></div>
    <div class="dots" style="left:255px;top:224px"><span></span><span></span><span></span></div>
  </section>
  <section class="about">
    <div class="art" role="img" aria-label="Illustration of browser windows joined by a chain link on a blue-teal blob" style="left:35px;top:20px;width:215px;height:215px;background:linear-gradient(135deg,#3a73dc,#10d0b3);border-radius:48% 52% 40% 60% / 55% 45% 55% 45%"></div>
    <h2 style="left:281px;top:36px">ABOUT US</h2><span class="rule" style="left:281px;top:56px"></span>
    <h3 style="left:281px;top:68px">Lorem ipsum dolor sit amet, consectetur</h3>
    <p style="left:281px;top:90px">Molestias excepturi sint occaecati cupiditate nonkuseopi iousesios provident, similique sunt in culpa qui officia deserunt mollitiaseiu animi, id est laborum et dolorum fuga.</p>
    <p style="left:281px;top:130px">Et harum quidem rerum facilis est et expedita distinctio. Nam libero tempore, cum soluta nobis est eligendi optio cumque nihil impedit quo minus id quod maxime placeat facere possimus, omnis voluptas.</p>
    <span class="btn btn--solid more" style="left:281px;top:183px">Read More</span>
  </section>
  <section class="services">
    <div class="sec-title" style="top:35px">Our Services</div><span class="rule" style="left:251px;top:55px"></span>
    <div class="sec-sub" style="top:61px">Lorem ipsum dolor sit amet, consectetur adipiscing elit, sed do eiusmod tempor incididunt</div>
    <div class="card" style="left:48px"><div class="icon" style="background:#fde3ea"><svg width="10" height="10" viewBox="0 0 24 24"><rect x="3" y="5" width="18" height="14" rx="2" fill="none" stroke="#e6497e" stroke-width="2"/></svg></div><h4>Backlinks</h4><p>Lorem ipsum dolor sit amet, consectetur adipiscing elit, sed do eiusmod tempor incididunt ut labore et dolore magna aliqua.</p><span class="btn btn--solid">Read More</span></div>
    <div class="card card--on" style="left:196px"><div class="icon" style="background:#fff"><svg width="10" height="10" viewBox="0 0 24 24"><rect x="3" y="4" width="18" height="16" rx="2" fill="none" stroke="#3b74d8" stroke-width="2"/><path d="M3 9h18" stroke="#3b74d8" stroke-width="2"/></svg></div><h4>Content writing</h4><p>Lorem ipsum dolor sit amet, consectetur adipiscing elit, sed do eiusmod tempor incididunt ut labore et dolore magna aliqua.</p><span class="btn btn--ghost">Read More</span></div>
    <div class="card" style="left:344px"><div class="icon" style="background:#dff5e6"><svg width="10" height="10" viewBox="0 0 24 24"><rect x="3" y="4" width="18" height="13" rx="2" fill="none" stroke="#3cb46e" stroke-width="2"/><path d="M8 21h8" stroke="#3cb46e" stroke-width="2"/></svg></div><h4>Digital PR for Links</h4><p>Lorem ipsum dolor sit amet, consectetur adipiscing elit, sed do eiusmod tempor incididunt ut labore et dolore magna aliqua.</p><span class="btn btn--solid">Read More</span></div>
    <div class="bar-dots" style="top:257px"><span></span><span></span></div>
  </section>
  <section class="testimonials">
    <div class="sec-title" style="top:37px">Testimonials</div><span class="rule" style="left:251px;top:57px"></span>
    <div class="sec-sub" style="top:63px">Lorem ipsum dolor sit amet, consectetur adipiscing elit, sed do eiusmod tempor incididunt</div>
    <span class="arrow" style="left:92px"><svg width="5" height="5" viewBox="0 0 10 10"><path d="M7 1L3 5l4 4" fill="none" stroke="#3b74d8" stroke-width="1.5"/></svg></span>
    <div class="quote-card"><div class="mark">“</div><p>Similique sunt in culpa qui officia deserunt mollitia animi, id est laborum et dolorum fuga. Et harum quidem rerum facilis est et expedita distinctio. Nam libero tempore, cum soluta nobis est eligendi optio cumque nihil impedit quo.</p><div class="person"><span class="av"></span><div><b>Dana Reyes</b><span>CEO, Northfield</span></div></div></div>
    <span class="arrow" style="left:421px"><svg width="5" height="5" viewBox="0 0 10 10"><path d="M3 1l4 4-4 4" fill="none" stroke="#3b74d8" stroke-width="1.5"/></svg></span>
  </section>
  <section class="stats">
    <div class="sec-title" style="top:36px">Customers Expectation</div><span class="rule" style="left:251px;top:56px"></span>
    <div class="sec-sub" style="top:62px">Lorem ipsum dolor sit amet, consectetur adipiscing elit, sed do eiusmod tempor incididunt</div>
    <div class="stat" style="left:68px"><b>120k</b><span>Downloaded</span></div>
    <div class="stat" style="left:162px"><b>7k</b><span>Feedback</span></div>
    <div class="stat" style="left:258px"><b>150+</b><span>Workers</span></div>
    <div class="stat" style="left:359px"><b>35+</b><span>Contributors</span></div>
    <div class="ask"><h5>HAVE ANY QUESTIONS ABOUT US?</h5><p>Don't hesitate to contact us</p><span class="btn btn--solid">Read More</span></div>
  </section>
  <section class="blog">
    <div class="sec-title" style="top:37px">Our Blog</div><span class="rule" style="left:251px;top:57px"></span>
    <div class="sec-sub" style="top:63px">Lorem ipsum dolor sit amet, consectetur adipiscing elit, sed do eiusmod tempor incididunt</div>
    <article class="post" style="left:48px"><div class="thumb" role="img" aria-label="Photo of wooden blocks with marketing icons on a desk" style="background:linear-gradient(135deg,#8a5a34,#c99b6c)"></div><div class="meta">Admin &nbsp; May 18, 2020</div><h6>Dignissimos Ucimus</h6><p>Lorem ipsum dolor sit amet, aseiu consectetur adipiscing elit, sed dsaeujo sei eiusmod tempor incididunt ut labore</p><a>Read More ›</a></article>
    <article class="post" style="left:196px"><div class="thumb" role="img" aria-label="Photo of a desk with a sketched link building note" style="background:linear-gradient(135deg,#d8d4cc,#f4f1ea)"></div><div class="meta">Admin &nbsp; May 18, 2020</div><h6>Dignissimos Ucimus</h6><p>Lorem ipsum dolor sit amet, aseiu consectetur adipiscing elit, sed dsaeujo sei eiusmod tempor incididunt ut labore</p><a>Read More ›</a></article>
    <article class="post" style="left:344px"><div class="thumb" role="img" aria-label="Photo of a keyboard with an orange web traffic key" style="background:linear-gradient(135deg,#3a3d44,#e9a23b)"></div><div class="meta">Admin &nbsp; May 18, 2020</div><h6>Dignissimos Ucimus</h6><p>Lorem ipsum dolor sit amet, aseiu consectetur adipiscing elit, sed dsaeujo sei eiusmod tempor incididunt ut labore</p><a>Read More ›</a></article>
  </section>
  <footer class="site-footer">
    <div class="brand"><i></i>Linkwise</div>
    <p class="f-about">architecto beatae vitae dicta sunt oisauerk explicabo. Nemo enim ipsam voluptatem quia voluptas sit aspernatur aut odit aut fugitsaeiu klasdmoix.</p>
    <div class="socials"><span></span><span></span><span></span></div>
    <div class="f-col" style="left:178px"><h6>Quick Links</h6><ul><li>Home</li><li>About Us</li><li>Services</li><li>Testimonials</li><li>Blog</li><li>Contact Us</li></ul></div>
    <div class="f-col" style="left:278px"><h6>Support</h6><ul><li>FAQ's</li><li>Privacy Policy</li><li>Terms &amp; Condition</li><li>Community</li><li>Contact Us</li></ul></div>
    <div class="f-col" style="left:380px"><h6>Address</h6><p class="addr"><b>Location:</b> 120 Harbor Lane, San Diego, CA 92101, USA</p><p class="addr"><b>Email:</b> hello@linkwise.example</p><p class="addr"><b>Phone:</b> +1 555 010 0142</p></div>
    <div class="copy">Copyright ©2020 All rights reserved</div>
  </footer>
</div>

</body>
</html>
```